Venture Capital Investment Firm

We are looking to overhaul our existing website (substantially), with only using the same logos (which we can provide).
We are an investment firm that focuses on making loans to late stage technology companies. Our site should ultimately look like other venture capital firms, and look modern and fresh. We have an existing website www.northvaleloan.com which this will be replacing, although we will be using a lot of the existing written content, and potentially the numbers of pages we will need, we are not wed to anything else. Please feel free to shoot any questions at any time and thank you in advance for your help!
Websites we like as examples:
https://www.tkbrandel.com/
https://www.emberwoodfunds.com/
Target Market(s)
Potential investors who will invest in our firm, as well as potentially companies that are looking to borrow money from us.

```html
<!DOCTYPE html>
<html lang="en">
<head>
<meta charset="utf-8">
<title>Northvale — Venture Capital Investment Firm</title>
<link rel="stylesheet" href="https://fonts.googleapis.com/css2?family=Cinzel:wght@400;600;700&family=Raleway:wght@400;500&display=swap">
<style>
  :root {
    --bg: #22142d;
    --bg-deep: #1c1026;
    --header-top: #2a1240;
    --header-bottom: #221530;
    --gold: #e3b31f;
    --gold-soft: #c99f2a;
    --text: #ece7f0;
    --muted: #c9c0d0;
    --line: #6d6277;
    --frame: #8a7f93;
    --field: #2a1637;
    --numeral: rgba(255,255,255,0.045);
  }
  * { box-sizing: border-box; margin: 0; padding: 0; }
  html, body { width: 1200px; height: 3748px; overflow: hidden; }
  body {
    position: relative;
    background: linear-gradient(180deg, #241532 0%, var(--bg) 40%, #22152b 100%);
    color: var(--text);
    font-family: "Raleway", sans-serif;
  }
  .abs { position: absolute; }
  .serif { font-family: "Cinzel", serif; }

  /* Header */
  .site-header {
    position: absolute; left: 0; top: 0; width: 1200px; height: 218px;
    background: linear-gradient(180deg, var(--header-top) 0%, var(--header-bottom) 100%);
  }
  .brand {
    position: absolute; left: 0; width: 1200px; top: 48px; text-align: center;
    font-family: "Cinzel", serif; font-weight: 600; font-size: 36px; color: var(--text);
    letter-spacing: 1px;
  }
  .brand-mark {
    display: inline-block; width: 14px; height: 14px; border-radius: 50%;
    background: var(--gold); margin-right: 12px; vertical-align: middle; position: relative; top: -4px;
  }
  .tagline {
    position: absolute; left: 0; width: 1200px; top: 119px; text-align: center;
    font-family: "Cinzel", serif; font-size: 9px; letter-spacing: 1px; color: var(--muted);
  }
  .rule { position: absolute; height: 1px; background: var(--line); }
  .top-contact {
    position: absolute; left: 860px; top: 39px; font-family: "Cinzel", serif;
    font-size: 10px; letter-spacing: 3px; color: var(--text);
  }
  .social {
    position: absolute; top: 36px; width: 18px; height: 18px; border-radius: 50%; background: var(--gold);
  }
  .nav a {
    position: absolute; top: 171px; font-family: "Cinzel", serif; font-size: 10px;
    letter-spacing: 4px; color: var(--text); text-decoration: none;
  }
  .nav a.active { color: var(--gold); }
  .nav a.active::after {
    content: ""; position: absolute; left: 0; right: 0; top: 19px; height: 1px; background: var(--gold);
  }

  /* Hero */
  .hero {
    position: absolute; left: 0; top: 218px; width: 1200px; height: 559px;
    background:
      linear-gradient(125deg, rgba(255,255,255,0.05) 0%, rgba(0,0,0,0) 35%),
      linear-gradient(235deg, rgba(255,255,255,0.05) 0%, rgba(0,0,0,0) 35%),
      radial-gradient(ellipse at 50% 70%, #231832 0%, #140b1c 70%);
  }
  .hero-title {
    position: absolute; left: 0; width: 1200px; top: 140px; text-align: center;
    font-family: "Cinzel", serif; font-size: 31px; letter-spacing: 3px; color: var(--text);
  }
  .hero-sub {
    position: absolute; left: 0; width: 1200px; top: 205px; text-align: center;
    font-family: "Cinzel", serif; font-size: 15px; letter-spacing: 1px; color: var(--text);
  }
  .btn {
    position: absolute; display: flex; align-items: center; justify-content: center;
    border: 1px solid var(--text); font-family: "Cinzel", serif; font-weight: 600;
    font-size: 10px; letter-spacing: 1px; color: var(--text);
  }
  .btn.gold { border-color: var(--gold-soft); }
  .btn.hero-btn { font-size: 12px; font-weight: 400; }

  /* Sections */
  .numeral {
    position: absolute; font-family: "Cinzel", serif; font-size: 118px; color: var(--numeral);
    line-height: 1;
  }
  .section-title {
    position: absolute; font-family: "Cinzel", serif; font-size: 24px; letter-spacing: 10px;
    color: var(--gold); line-height: 1;
  }
  .title-rule { position: absolute; height: 1px; background: var(--gold-soft); }
  .subhead {
    position: absolute; font-family: "Cinzel", serif; font-size: 12px; letter-spacing: 0.5px; color: var(--text);
  }
  .copy {
    position: absolute; font-size: 8.5px; line-height: 22.5px; letter-spacing: 0.4px;
    text-transform: uppercase; color: var(--muted);
  }
  .frame { position: absolute; border: 1px solid var(--frame); background: var(--bg-deep); }
  .frame.selected { border-color: var(--gold-soft); }
  .fill-art { position: absolute; }
  .divider { position: absolute; left: 150px; width: 899px; height: 1px; background: var(--line); }

  /* Team */
  .portrait {
    position: absolute; left: 31px; top: 30px; width: 135px; height: 134px;
    background: linear-gradient(180deg, #2c1548 0%, #5a5560 60%, #3a3540 100%);
  }
  .bio-card { position: absolute; left: 202px; top: 2451px; width: 796px; height: 393px; border: 1px solid var(--frame); background: #261537; }
  .bio-name {
    position: absolute; left: 45px; top: 40px; font-family: "Cinzel", serif; font-weight: 700;
    font-size: 16px; letter-spacing: 3px; color: var(--text);
  }
  .bio-role { position: absolute; left: 45px; top: 78px; font-family: "Cinzel", serif; font-size: 11px; letter-spacing: 1px; color: var(--muted); }

  /* Contact */
  .label {
    position: absolute; width: 200px; left: 188px; text-align: right;
    font-family: "Cinzel", serif; font-size: 15px; letter-spacing: 1.5px; color: var(--text);
  }
  .field {
    position: absolute; left: 426px; width: 352px; height: 52px; border: 1px solid var(--frame);
    background: var(--field); font-size: 8px; letter-spacing: 1px; color: var(--muted);
    padding: 22px 0 0 24px; text-transform: uppercase;
  }
  .field.message { height: 157px; background: #e9e7ea; border-color: #e9e7ea; }
</style>
</head>
<body>

<header class="site-header">
  <div class="brand"><span class="brand-mark"></span>Northvale</div>
  <div class="rule" style="left:75px;top:125px;width:412px"></div>
  <div class="rule" style="left:713px;top:125px;width:411px"></div>
  <div class="tagline">Venture Capital Investment Firm</div>
  <div class="top-contact">CONTACT</div>
  <span class="social" style="left:949px" role="img" aria-label="Social link"></span>
  <span class="social" style="left:987px" role="img" aria-label="Social link"></span>
  <span class="social" style="left:1025px" role="img" aria-label="Social link"></span>
  <nav class="nav">
    <a class="active" style="left:157px">HOME</a>
    <a style="left:273px">STRATEGY</a>
    <a class="active" style="left:428px">ABOUT US</a>
    <a style="left:579px">TEAM</a>
    <a style="left:694px">NEWS</a>
    <a style="left:810px">CONTACT</a>
    <a style="left:956px">INVESTORS</a>
  </nav>
</header>

<section class="hero" role="img" aria-label="Dark architectural photograph of converging beams">
  <h1 class="hero-title">A GLOBAL STRUCTURED CREDIT INVESTMENT FIRM</h1>
  <p class="hero-sub">OUR FOCUS IS ON THE HEALTHCARE AND TECHNOLOGY INDUSTRIES</p>
  <div class="btn hero-btn" style="left:460px;top:335px;width:261px;height:110px">LEARN MORE</div>
</section>

<!-- Strategy -->
<div class="numeral" style="left:160px;top:832px">01</div>
<h2 class="section-title" style="left:157px;top:884px">THE STRATEGY</h2>
<div class="title-rule" style="left:259px;top:943px;width:172px"></div>
<p class="subhead" style="left:160px;top:981px">WE PROVIDE FLEXIBLE CAPITAL TO INNOVATIVE COMPANIES AND THEIR INVESTORS</p>
<p class="copy" style="left:160px;top:1060px;width:580px">
  Our focus spans the life science and technology industries, two sectors where intellectual property (IP)
  is an integral driver of asset and enterprise value.<br>
  Our broad experience in investing, technology evaluation, and product forecasting affords us a unique
  understanding of the value of assets in these dynamic sectors, allowing us to see value where others
  cannot.
</p>
<div class="btn gold" style="left:157px;top:1239px;width:226px;height:74px">LEARN MORE</div>
<div class="frame" style="left:781px;top:924px;width:262px;height:343px">
  <div class="fill-art" role="img" aria-label="Gold chess knight icon" style="left:95px;top:120px;width:72px;height:102px;background:linear-gradient(180deg,#f6d55a,#e3b31f);border-radius:30px 10px 4px 4px"></div>
</div>

<div class="divider" style="top:1389px"></div>

<!-- Who are we -->
<div class="numeral" style="left:856px;top:1406px">02</div>
<h2 class="section-title" style="left:766px;top:1461px">WHO ARE WE</h2>
<div class="title-rule" style="left:803px;top:1518px;width:211px"></div>
<div class="frame" style="left:157px;top:1491px;width:262px;height:345px">
  <div class="fill-art" role="img" aria-label="Gold businessman icon" style="left:79px;top:124px;width:106px;height:98px;background:linear-gradient(180deg,#f6d55a,#d9ad1f);border-radius:40px 40px 6px 6px"></div>
</div>
<p class="subhead" style="left:490px;top:1560px">OUR SIMPLE IDEA : FINANCE PROVEN INNOVATION WITH A DIFFERENT APPROACH</p>
<p class="copy" style="left:490px;top:1638px;width:550px">
  Northvale Loan is a private investment firm unique in its dual focus on life science and technology credit
  opportunities. Our ambidextrous approach to investing reflects a broad recognition and
  appreciation for the critical role intellectual property plays in the successful commercialization
  of products. We apply our extensive industry expertise to assess the revenue visibility created by
  these assets and offer a range of creative financing solutions.
</p>
<div class="btn" style="left:759px;top:1818px;width:224px;height:73px">LEARN MORE</div>

<div class="divider" style="top:1967px"></div>

<!-- Team -->
<div class="numeral" style="left:160px;top:2022px">03</div>
<h2 class="section-title" style="left:164px;top:2078px">MEET OUR TEAM</h2>
<div class="title-rule" style="left:259px;top:2134px;width:211px"></div>

<div class="frame selected" style="left:202px;top:2180px;width:195px;height:194px">
  <div class="portrait" role="img" aria-label="Portrait of managing partner"></div>
</div>
<div class="frame" style="left:503px;top:2180px;width:195px;height:194px">
  <div class="portrait" role="img" aria-label="Portrait of team member"></div>
</div>
<div class="frame" style="left:804px;top:2180px;width:195px;height:194px">
  <div class="portrait" role="img" aria-label="Portrait of team member"></div>
</div>
<svg class="abs" style="left:277px;top:2402px" width="32" height="20" viewBox="0 0 32 20">
  <polyline points="1,1 16,19 31,1" fill="none" stroke="#c99f2a" stroke-width="1.2"/>
</svg>

<article class="bio-card">
  <h3 class="bio-name">ELIAS MARREN</h3>
  <span class="abs" style="left:241px;top:42px;width:17px;height:17px;border-radius:50%;background:var(--gold)" role="img" aria-label="Profile link"></span>
  <svg class="abs" style="left:273px;top:44px" width="18" height="13" viewBox="0 0 18 13">
    <rect x="0" y="0" width="18" height="13" fill="#e3b31f"/>
    <polyline points="0,0 9,7 18,0" fill="none" stroke="#261537" stroke-width="1.4"/>
  </svg>
  <p class="bio-role">MANAGING PARTNER</p>
  <p class="copy" style="left:45px;top:126px;width:720px">
    Elias Marren is an industry leader with over $1.2B in structured credit investments since 2004. Elias focuses on origination,
    underwriting, and portfolio management across sectors at Northvale Loan.<br>
    Mr. Marren was the co-founder of Brightwell Health Partners, a life sciences focused structured credit fund, from 2010-2014.
    From 2004-2010, Mr. Marren was managing director and co-head of the healthcare group for the Keystone Special Situations
    Fund at Harborline Investment Group.
  </p>
  <div class="btn" style="left:297px;top:274px;width:224px;height:74px">LEARN MORE</div>
</article>

<div class="divider" style="top:2921px"></div>

<!-- Contact -->
<h2 class="section-title" style="left:0;width:1200px;text-align:center;top:3029px;padding-left:10px">CONTACT US</h2>
<form>
  <span class="label" style="top:3130px">NAME</span>
  <div class="field" style="top:3113px">First</div>
  <div class="field" style="top:3188px">Last</div>
  <span class="label" style="top:3281px">EMAIL</span>
  <div class="field" style="top:3264px"></div>
  <span class="label" style="top:3357px">PHONE</span>
  <div class="field" style="top:3340px"></div>
  <span class="label" style="top:3433px">MESSAGE</span>
  <div class="field message" style="top:3415px"></div>
  <div class="btn" style="left:490px;top:3611px;width:224px;height:75px">SUBMIT</div>
</form>

</body>
</html>
```